QLM Stationery Design Project

Dear Designers,
We need a new stationery design for company to match our new logo.
Designers should provide a design for the following:
1. Business Card: 3.5x2 Inches.
2. Letterhead: A4 size.
3. Envelops: 25x35.5 Cm.
You can keep the Arabic name at the bottom of the logo Or you can use the separate attached Arabic Name.
Please refer to the attached logo guide for design information.
Sample Business Card information:
Name: Tariq Saleem
Position: Operation Manager
Tel: +966 920004717 Ex. 500
Fax: +966 (3)8462153
Mob: +966 (5)00387260
email: tariq@qlm-example.com.sa
URL: www.qlm-example.com.sa
Address:
Le Verger Tower, Suite 517
Nasser bin Omar Str.
Khobar, 34861
Saudi Arabia
Updates
Dear All,
Please note, we had uploaded our logo along with Arabic writing in Adobe illustrator format (.ai).
Regards,
Yousef
Dear All,
A sample data for the business card had been added as per your request.
Regards,
Yousef

```html
<!DOCTYPE html>
<html lang="en">
<head>
<meta charset="utf-8">
<title>QLM Business Card</title>
<link rel="stylesheet" href="https://fonts.googleapis.com/css2?family=Open+Sans:wght@400;600;700&display=swap">
<style>
  :root {
    --backdrop: #e8e5e1;
    --card-navy: #0f2e54;
    --ink-white: #ffffff;
    --ink-muted: #b3bccb;
    --rule: #7f8ea6;
  }
  * { box-sizing: border-box; margin: 0; padding: 0; }
  html, body {
    width: 1200px; height: 472px; overflow: hidden;
    background: var(--backdrop);
    font-family: "Open Sans", Arial, sans-serif;
  }
  .stage { position: relative; width: 1200px; height: 472px; }
  .card {
    position: absolute; top: 85px; width: 525px; height: 298px;
    background: var(--card-navy); border-radius: 14px; color: var(--ink-white);
  }
  .card--front { left: 57px; }
  .card--back { left: 606px; }

  .brand { position: absolute; display: flex; align-items: center; gap: 12px; }
  .brand__dot { width: 18px; height: 18px; border-radius: 50%; background: var(--ink-white); }
  .brand__name { font-weight: 700; color: var(--ink-white); letter-spacing: 2px; line-height: 1; }
  .card--front .brand { left: 40px; top: 72px; }
  .card--front .brand__name { font-size: 54px; }
  .card--back .brand { left: 50%; top: 100px; transform: translateX(-50%); }
  .card--back .brand__name { font-size: 62px; }

  .holder { position: absolute; left: 43px; top: 202px; font-size: 14px; }
  .holder__name { font-weight: 700; }
  .holder__title { color: var(--ink-muted); font-size: 12px; }

  .contact {
    position: absolute; left: 46px; top: 234px;
    display: flex; align-items: stretch; font-size: 12.2px; color: var(--ink-muted); line-height: 18px;
  }
  .contact__col { padding: 0 10px; }
  .contact__col:first-child { padding-left: 0; }
  .contact__col + .contact__col { border-left: 1px solid var(--rule); }
  .contact__row { display: flex; align-items: center; gap: 6px; white-space: nowrap; }
  .contact__icon { width: 10px; height: 10px; fill: var(--ink-muted); }

  .site {
    position: absolute; left: 0; right: 0; top: 236px; text-align: center;
    font-size: 12px; letter-spacing: 2.6px; color: var(--ink-white);
  }
</style>
</head>
<body>
<main class="stage">
  <section class="card card--front">
    <div class="brand"><span class="brand__dot"></span><span class="brand__name">QLM</span></div>
    <p class="holder"><span class="holder__name">YOUR NAME,</span> <span class="holder__title">Title</span></p>
    <div class="contact">
      <div class="contact__col">
        <p class="contact__row">Street Name, City Name</p>
        <p class="contact__row">State, City Zip 123 4560</p>
      </div>
      <div class="contact__col">
        <p class="contact__row">
          <svg class="contact__icon" viewBox="0 0 10 10" aria-hidden="true"><path d="M2 0.5l2 2-1 1.2c.6 1.3 1.6 2.3 2.9 2.9l1.2-1 2 2-1.4 1.9C4.3 9.3.7 5.7.2 1.9z"/></svg>123-456-7890
        </p>
        <p class="contact__row">
          <svg class="contact__icon" viewBox="0 0 10 10" aria-hidden="true"><rect x="2.5" y="0" width="5" height="10" rx="1"/><rect x="3.4" y="1.2" width="3.2" height="6" fill="#0f2e54"/></svg>123-456-7890
        </p>
      </div>
      <div class="contact__col">
        <p class="contact__row">
          <svg class="contact__icon" viewBox="0 0 10 10" aria-hidden="true"><rect x="0" y="2" width="10" height="7" rx="1"/><path d="M0.5 2.5l4.5 3.5 4.5-3.5" fill="none" stroke="#0f2e54" stroke-width="1"/></svg>info@qlm-example.com.sa
        </p>
        <p class="contact__row">
          <svg class="contact__icon" viewBox="0 0 10 10" aria-hidden="true"><circle cx="5" cy="5" r="5"/><path d="M0 5h10M5 0c-2 2.5-2 7.5 0 10M5 0c2 2.5 2 7.5 0 10" fill="none" stroke="#0f2e54" stroke-width="0.8"/></svg>www.website.com
        </p>
      </div>
    </div>
  </section>

  <section class="card card--back">
    <div class="brand"><span class="brand__dot"></span><span class="brand__name">QLM</span></div>
    <p class="site">www.website.com</p>
  </section>
</main>
</body>
</html>
```